Stationery Design for Family Law Firm
BROOK VESTAL, LLP
Stationery Design for Family Law Firm -
Creative Brief
Professional
Martin D. Vestal
Attorney & Counselor at Law
4187 Larkin Street San Diego, CA 92104
martin@brookvestal-law.example
www.brookvestal-law.example
Paper will be ivory. Please use large and small caps for name and "Attorney & Counselor" at Law. Sentence case for the rest.
Family Law I Guardianships I Conservatorships I Estate Planning

```html
<!DOCTYPE html>
<html lang="en">
<head>
<meta charset="utf-8">
<title>Brook Vestal, LLP — Business Cards</title>
<link rel="stylesheet" href="https://fonts.googleapis.com/css2?family=Cinzel:wght@400;600&display=swap">
<style>
  :root {
    --backdrop: #3a3a3c;
    --ivory: #fbfaf6;
    --ink-black: #141414;
    --firm-blue: #2f6aa5;
    --deep-blue: #1f4f84;
    --text-white: #ffffff;
    --text-gray: #4a4a4a;
  }
  * { margin: 0; padding: 0; box-sizing: border-box; }
  html, body { width: 1200px; height: 713px; overflow: hidden; }
  body {
    background: var(--backdrop);
    font-family: "Cinzel", "Times New Roman", serif;
    position: relative;
  }
  .card {
    position: absolute;
    width: 485px;
    height: 285px;
    border-radius: 16px;
    overflow: hidden;
    box-shadow: 0 4px 14px rgba(0,0,0,0.45);
  }
  .card--front-light { left: 91px; top: 53px; background: var(--ivory); }
  .card--back-light  { left: 629px; top: 53px; background: var(--ivory); }
  .card--front-dark  { left: 91px; top: 365px; background: var(--ink-black); }
  .card--back-dark   { left: 629px; top: 365px; background: var(--ink-black); }

  .wave { position: absolute; inset: 0; width: 100%; height: 100%; }

  .firm-name {
    font-weight: 600;
    color: var(--firm-blue);
    letter-spacing: 1px;
    line-height: 1;
    display: flex;
    align-items: center;
    gap: 8px;
  }
  .firm-name .mark {
    width: 12px; height: 12px; border-radius: 50%;
    background: var(--firm-blue);
    flex: none;
  }
  .firm-tagline {
    font-variant: small-caps;
    font-size: 11px;
    letter-spacing: 0.6px;
    margin-top: 6px;
  }

  .front-logo { position: absolute; left: 26px; top: 38px; }
  .front-logo .firm-name { font-size: 21px; }
  .card--front-light .firm-tagline { color: var(--text-gray); }
  .card--front-dark .firm-tagline { color: var(--text-white); }

  .back-logo {
    position: absolute; left: 0; right: 0; top: 92px;
    display: flex; flex-direction: column; align-items: center;
  }
  .back-logo .firm-name { font-size: 27px; }
  .back-logo .firm-tagline { font-size: 12px; }
  .card--back-light .firm-tagline { color: var(--text-gray); }
  .card--back-dark .firm-tagline { color: var(--text-white); }

  .services {
    position: absolute; left: 0; right: 0; top: 200px;
    text-align: center;
    font-size: 10.5px;
    letter-spacing: 0.4px;
  }
  .card--back-light .services { color: var(--firm-blue); }
  .card--back-dark .services { color: var(--text-white); }

  .person { position: absolute; left: 28px; top: 204px; color: var(--text-white); }
  .person-name { font-size: 18px; font-variant: small-caps; letter-spacing: 0.8px; }
  .person-title { font-size: 11px; font-variant: small-caps; letter-spacing: 0.5px; margin-top: 4px; }

  .contact {
    position: absolute; left: 262px; top: 186px;
    color: var(--text-white);
    font-style: normal;
    font-size: 10.5px;
    line-height: 15px;
    font-variant: small-caps;
    letter-spacing: 0.3px;
  }
</style>
</head>
<body>

  <!-- Front, light -->
  <section class="card card--front-light">
    <svg class="wave" viewBox="0 0 485 285" aria-hidden="true">
      <path d="M0 150 C120 135 230 200 485 125 L485 285 L0 285 Z" fill="var(--firm-blue)"/>
      <path d="M0 112 C110 104 190 158 330 150 C210 166 120 130 0 136 Z" fill="var(--ink-black)"/>
    </svg>
    <div class="front-logo">
      <div class="firm-name"><span class="mark"></span>BROOK VESTAL, LLP</div>
      <div class="firm-tagline">Attorneys &amp; Counselors at Law</div>
    </div>
    <div class="person">
      <div class="person-name">Martin D. Vestal</div>
      <div class="person-title">Attorney &amp; Counselor at Law</div>
    </div>
    <address class="contact">
      4187 Larkin Street<br>
      San Diego, CA 92104<br>
      Phone: (619) 555-0147<br>
      Email: martin@brookvestal-law.example<br>
      Web: www.brookvestal-law.example
    </address>
  </section>

  <!-- Back, light -->
  <section class="card card--back-light">
    <div class="back-logo">
      <div class="firm-name"><span class="mark"></span>BROOK VESTAL, LLP</div>
      <div class="firm-tagline">Attorneys &amp; Counselors at Law</div>
    </div>
    <p class="services">Family Law I Guardianships I Conservatorships I Estate Planning</p>
  </section>

  <!-- Front, dark -->
  <section class="card card--front-dark">
    <svg class="wave" viewBox="0 0 485 285" aria-hidden="true">
      <path d="M0 150 C120 135 230 200 485 125 L485 285 L0 285 Z" fill="var(--firm-blue)"/>
      <path d="M0 112 C110 104 190 158 330 150 C210 166 120 130 0 136 Z" fill="var(--ivory)"/>
    </svg>
    <div class="front-logo">
      <div class="firm-name"><span class="mark"></span>BROOK VESTAL, LLP</div>
      <div class="firm-tagline">Attorneys &amp; Counselors at Law</div>
    </div>
    <div class="person">
      <div class="person-name">Martin D. Vestal</div>
      <div class="person-title">Attorney &amp; Counselor at Law</div>
    </div>
    <address class="contact">
      4187 Larkin Street<br>
      San Diego, CA 92104<br>
      Phone: (619) 555-0147<br>
      Email: martin@brookvestal-law.example<br>
      Web: www.brookvestal-law.example
    </address>
  </section>

  <!-- Back, dark -->
  <section class="card card--back-dark">
    <div class="back-logo">
      <div class="firm-name"><span class="mark"></span>BROOK VESTAL, LLP</div>
      <div class="firm-tagline">Attorneys &amp; Counselors at Law</div>
    </div>
    <p class="services">Family Law I Guardianships I Conservatorships I Estate Planning</p>
  </section>

</body>
</html>
```